Health and Wellbeing online Shop

I have attached a specification, however in summary this is a new business startup selling vitamins and supplements.

We need a web design for new wellbeing website, selling high end vitamins, supplements and nootropics. Therefore I need a simple eCommerce solution .

I need the website to look very different to other websites on the market. The more creative the better. It should look fresh elegant and simple. The criteria for products being on my site is that they have great reviews and they have been scientifically tested.

You will need the option of being able to log into an account, either through loopbook, vorkle, chirply, Pictoreel or create an account with email. For accounts, users will need the facility to reset passwords, see previous orders, track current order, and maintain favourites.

It should be PC, mobile and tablet friendly.

Look and Feel

It should be an elegant, modern, professional, trendy, unisex website. It should look clean and calm. Am happy to try interesting and slightly unusual designs. I would also like to have chat functionality, either powered by kabUNtalk or by Rok 58.

Websites I like are
https://www.prime-glowforms.co.uk/
https://www.onlytonics.co.uk/
http://www.clearmedora.com/

PLEASE DO USE YOUR KNOWELDGE OF WHAT WORKS FOR WEB DESIGN. YOU’RE THE EXPERT AND NEED YOUR EXPERTISE. CARTE BLANCHE TO DESIGN AS YOU SEE FIT. Please be creative, I need my site to stand out from the crowd.

Target Market(s)
Middle aged women are our most common client, however, younger patients, both male and female, will often visit the site. In summary, I would like the site to appeal to all age brackets.

Industry/Entity Type
Business

Coding
Coded - Design and coding required

Number of Pages Required
5 pages
Updates

I would like more designs. I was expecting 75+ Designs to choose from as per the package I paid for.

Target Market(s)

Industry/Entity Type

Health And Wellness

Coding

Number of Pages Required

5+ page

Requirements
Must have
• Creative design

```html
<!DOCTYPE html>
<html lang="en">
<head>
<meta charset="utf-8">
<title>Kalvio – Shopping Cart</title>
<link rel="stylesheet" href="https://fonts.googleapis.com/css2?family=Crimson+Pro:wght@400;500&family=Jost:wght@300;400&display=swap">
<style>
  :root {
    --ink: #111111;
    --muted: #7a7a7a;
    --rule: #8c8c8c;
    --cell-rule: #9a9a9a;
    --paper: #ffffff;
    --footer-bg: #808080;
    --footer-ink: #ffffff;
    --button-bg: #000000;
    --button-ink: #ffffff;
  }
  * { box-sizing: border-box; margin: 0; padding: 0; }
  html, body { width: 1200px; height: 1200px; overflow: hidden; background: var(--paper); }
  body {
    position: relative;
    font-family: "Crimson Pro", Georgia, serif;
    color: var(--ink);
    font-variant-numeric: oldstyle-nums;
  }
  .abs { position: absolute; }

  /* Header */
  .brand { left: 88px; top: 283px; display: flex; align-items: center; gap: 10px; }
  .brand-dot {
    width: 14px; height: 14px; border-radius: 50%;
    border: 1.5px solid var(--ink);
  }
  .brand-name { font-size: 26px; font-weight: 400; letter-spacing: 1px; line-height: 1; }
  .brand-tagline {
    margin-left: 10px;
    font-family: "Jost", Arial, sans-serif; font-weight: 300;
    font-size: 14px; letter-spacing: 0.2px; color: #333;
  }
  .brand-tagline .sep { margin: 0 6px; }
  .search-label { left: 544px; top: 295px; font-size: 17px; color: #333; }
  .search-field {
    left: 600px; top: 292px; width: 280px; height: 27px;
    border: 1px solid var(--rule); border-radius: 14px;
  }
  .account-link { top: 292px; font-size: 17px; }
  .login { left: 912px; }
  .signup { left: 979px; }
  .cart-icon { left: 1066px; top: 292px; }
  .cart-count {
    left: 1093px; top: 296px; width: 24px; height: 16px; border-radius: 8px;
    background: #1a1a1a; color: #fff; font-size: 13px;
    display: flex; align-items: center; justify-content: center;
  }
  .rule { left: 0; width: 1200px; height: 0; border-top: 1.5px solid var(--rule); }
  .rule-top { top: 340px; }
  .rule-nav { top: 380px; }
  .rule-title { top: 424px; border-top: 1px solid #333; }

  .main-nav { top: 352px; left: 0; width: 1200px; font-size: 12.5px; letter-spacing: 0.3px; }
  .main-nav a { position: absolute; color: var(--ink); text-decoration: none; }

  .page-title { left: 88px; top: 389px; font-size: 24px; font-weight: 400; }

  /* Cart table */
  .cart-table {
    left: 88px; top: 463px; width: 608px;
    border-collapse: collapse; table-layout: fixed;
  }
  .cart-table th, .cart-table td {
    border: 1px solid var(--cell-rule); height: 45px;
    vertical-align: middle; font-weight: 400;
  }
  .cart-table th { color: var(--muted); font-size: 18px; text-align: center; }
  .cart-table td { font-size: 18px; }
  .col-remove { width: 44px; text-align: center; }
  .col-name { width: 423px; padding-left: 10px; white-space: nowrap; }
  .col-qty { width: 45px; text-align: center; }
  .col-price { text-align: center; font-size: 22px !important; }
  .tm { font-size: 9px; vertical-align: 7px; }

  /* Totals */
  .totals {
    left: 895px; top: 463px; width: 217px;
    border-collapse: collapse; table-layout: fixed;
  }
  .totals th, .totals td { border: 1px solid var(--cell-rule); height: 45px; font-weight: 400; }
  .totals .totals-head { font-size: 24px; text-align: center; }
  .totals .label { width: 131px; text-align: center; font-size: 18px; }
  .totals .amount { text-align: center; font-size: 23px; }

  /* Buttons */
  .btn {
    top: 735px; width: 163px; height: 33px; border-radius: 17px;
    background: var(--button-bg); color: var(--button-ink);
    font-size: 16.5px; display: flex; align-items: center; justify-content: center;
  }
  .btn-continue { left: 88px; }
  .btn-modify { left: 532px; }
  .btn-checkout { left: 949px; }

  /* Footer */
  .site-footer {
    left: 0; top: 807px; width: 1200px; height: 127px;
    background: var(--footer-bg); color: var(--footer-ink);
    box-shadow: 0 8px 8px rgba(0,0,0,0.35);
  }
  .footer-col { position: absolute; top: 18px; }
  .footer-col h4 {
    font-weight: 400; font-size: 16px;
    border-bottom: 1px solid var(--footer-ink); padding-bottom: 1px;
    display: inline-block; margin-bottom: 5px;
  }
  .footer-col li { list-style: none; font-size: 10.5px; line-height: 14.5px; }
</style>
</head>
<body>
  <div class="abs brand">
    <div class="brand-dot"></div>
    <div class="brand-name">Kalvio</div>
    <div class="brand-tagline">RESTORE<span class="sep">|</span>REFINE<span class="sep">|</span>RENEW</div>
  </div>

  <div class="abs search-label">Search</div>
  <div class="abs search-field"></div>
  <a class="abs account-link login">Log In</a>
  <a class="abs account-link signup">Sign Up</a>
  <svg class="abs cart-icon" width="24" height="22" viewBox="0 0 24 22" fill="none" stroke="#111" stroke-width="1.4">
    <path d="M1 2h3l3 12h12l3-9H6"/>
    <circle cx="9" cy="18" r="2"/>
    <circle cx="18" cy="18" r="2"/>
  </svg>
  <div class="abs cart-count">0</div>

  <div class="abs rule rule-top"></div>
  <nav class="abs main-nav">
    <a style="left:563px">VITAMINS</a>
    <a style="left:683px">NOOTROPICS</a>
    <a style="left:829px">ABOUT US</a>
    <a style="left:952px">CONTACT US</a>
  </nav>
  <div class="abs rule rule-nav"></div>

  <h1 class="abs page-title">Shopping Cart</h1>
  <div class="abs rule rule-title"></div>

  <table class="abs cart-table">
    <thead>
      <tr><th class="col-remove"></th><th class="col-name" style="padding-left:0">Product Name</th><th class="col-qty">Qty</th><th>Unit Price</th></tr>
    </thead>
    <tbody>
      <tr><td class="col-remove">X</td><td class="col-name">Flexi-Core<span class="tm">TM</span> Care 1500mg Glucosamine x 180 tablets</td><td class="col-qty">1</td><td class="col-price">$11.89</td></tr>
      <tr><td class="col-remove">X</td><td class="col-name">Flexi-Core<span class="tm">TM</span> Care 1500mg Glucosamine x 180 tablets</td><td class="col-qty">1</td><td class="col-price">$11.89</td></tr>
      <tr><td class="col-remove">X</td><td class="col-name">Flexi-Core<span class="tm">TM</span> Care 1500mg Glucosamine x 180 tablets</td><td class="col-qty">1</td><td class="col-price">$11.89</td></tr>
      <tr><td class="col-remove">X</td><td class="col-name">Flexi-Core<span class="tm">TM</span> Care 1500mg Glucosamine x 180 tablets</td><td class="col-qty">1</td><td class="col-price">$11.89</td></tr>
    </tbody>
  </table>

  <table class="abs totals">
    <tr><th class="totals-head" colspan="2">Cart Totals</th></tr>
    <tr><td class="label">Sub Totals</td><td class="amount">$47.56</td></tr>
    <tr><td class="label">Grand Totals</td><td class="amount">$47.56</td></tr>
  </table>

  <a class="abs btn btn-continue">Continue Shopping</a>
  <a class="abs btn btn-modify">Modify Cart</a>
  <a class="abs btn btn-checkout">Checkout</a>

  <footer class="abs site-footer">
    <div class="footer-col" style="left:88px">
      <h4>Help &amp; Information</h4>
      <ul><li>About Us</li><li>Careers at NORVA</li><li>Corporate Responsibility</li><li>Investors Site</li></ul>
    </div>
    <div class="footer-col" style="left:396px">
      <h4>About Kalvio</h4>
      <ul><li>About Us</li><li>Careers at NORVA</li><li>Corporate Responsibility</li><li>Investors Site</li></ul>
    </div>
    <div class="footer-col" style="left:704px">
      <h4>More From Kalvio</h4>
      <ul><li>About Us</li><li>Careers at NORVA</li><li>Corporate Responsibility</li><li>Investors Site</li></ul>
    </div>
    <div class="footer-col" style="left:1012px">
      <h4>Our Partners</h4>
      <ul><li>About Us</li><li>Careers at NORVA</li><li>Corporate Responsibility</li><li>Investors Site</li></ul>
    </div>
  </footer>
</body>
</html>
```